Business Card Upgrade

I have designed our business card using our new logo. I think it needs imporovements. We used to have two cards for our business. One card was for our software business, and the other was for our consulting business. We are now in the process of combining our websites, marketing, name, and a new logo.

Our goal is to have a really sharp professional logo. One reason I designed the card the way I did was that our Titles are sometimes long, and by separating the person's name and title, it shows up very well and the title can be adjusted no matter how long it is. Sometimes the title can be 4 or 5 words or more.

We really like our logo on black as it shows up very nice. Our PMS colors are as follows: 368C and 459C.

The Designer that will be working with us will need to deliver the following:

The front and back of the Business Card Design will need to be delivered in a high quality JPEG, and
The front and back of the Business Card Design in Illustrator Format .ai
Any fonts will need to be sent to us if they are not standard and are required to open the Illustrator file correctly.

To help us get a good idea of the card with a title, please use the title: " Director of Software Development "

NOTE: The chosen designer will be selected to design our new letterhead within 2 weeks from the closing of this contest.

To help us make sure the card design works with longer titles, please use the followign job title on the card:  

"Director of Software and Product Development"

 

ALL DESIGNERS:

1. I appreciate the different angles you are showing the cards, but please be sure and always show the direct view, so I can see the layout and what the person I hand the card will see.

2. Please do not use white.  Please use off white as I don't care for white cards and they get dirty easy and do not represent the designs well.

Dear Designers,

Please provide samples straight one as a viewer of the card will see.  Some of the angles that are presented make it impossible to tell how everything fits, and sometimes even makes areas look skewed. So, please provide a straight sample view.

Pinnacle 400 company executives such as Vice Presidents, and Directors

Software

• Professional looking Card.

Our customers are Directors, Vice Presidents, and Presidents of companies as large as Pinnacle 400 companies. The card needs to get attention wile still looking professional.

Delivery of the finished product in Illustrator Format with any fonts needed to edit the text or open the file.

The card will be a heavy stock with a soft touch coating for that silk feel.

```html
<!DOCTYPE html>
<html lang="en">
<head>
<meta charset="utf-8">
<title>Kestrel Trade Group – Business Card</title>
<link rel="stylesheet" href="https://fonts.googleapis.com/css2?family=Open+Sans:wght@300;400;600;700;800&display=swap">
<style>
  :root {
    --paper: #ffffff;
    --frame: #222222;
    --card: #000000;
    --offwhite: #ececec;
    --offwhite-soft: #d9d9d9;
    --green: #4fe10c;
    --lime: #6fe000;
  }
  * { margin: 0; padding: 0; box-sizing: border-box; }
  html, body { width: 1015px; height: 1200px; overflow: hidden; background: var(--paper); }
  body { font-family: "Open Sans", Arial, sans-serif; position: relative; }
  .sheet { position: absolute; inset: 0; border: 1px solid var(--frame); }
  .card { position: absolute; background: var(--card); overflow: hidden; }
  .card--front { left: 42px; top: 48px; width: 932px; height: 548px; }
  .card--back  { left: 39px; top: 605px; width: 932px; height: 547px; }

  .accent-rule {
    position: absolute; left: 0; right: 0; height: 4px;
    background: var(--green);
  }
  .card--front .accent-rule { top: 372px; }
  .card--back .accent-rule { top: 392px; }

  .job-title {
    position: absolute; left: 0; right: 0; top: 82px;
    text-align: center;
    font-weight: 300; font-size: 28px; letter-spacing: 1px;
    color: var(--offwhite);
  }
  .person-name {
    position: absolute; left: 0; right: 0; top: 160px;
    text-align: center;
    font-weight: 700; font-size: 84px; line-height: 1;
    color: var(--offwhite);
  }
  .person-role {
    position: absolute; left: 0; right: 60px; top: 252px;
    text-align: center;
    font-weight: 700; font-size: 54px; line-height: 1;
    color: var(--offwhite-soft);
  }
  .contact {
    position: absolute; right: 23px; top: 394px;
    text-align: right; font-style: normal;
    font-weight: 700; font-size: 24px; line-height: 32px;
    color: var(--offwhite);
  }
  .brand-small {
    position: absolute; left: 36px; top: 488px;
    font-weight: 800; font-size: 30px; line-height: 1; letter-spacing: 1px;
    color: var(--green);
  }
  .brand-small::before {
    content: ""; display: inline-block; width: 16px; height: 16px;
    background: var(--green); margin-right: 10px; vertical-align: 3px;
  }
  .brand-large {
    position: absolute; left: 0; right: 0; top: 200px;
    text-align: center;
    font-weight: 800; font-size: 64px; line-height: 1; letter-spacing: 2px;
    color: var(--green);
  }
  .website {
    position: absolute; left: 68px; top: 470px;
    font-weight: 800; font-size: 54px; line-height: 1;
    color: var(--lime);
  }
</style>
</head>
<body>
<div class="sheet">
  <section class="card card--front" aria-label="Card front">
    <div class="accent-rule" aria-hidden="true"></div>
    <p class="job-title">“Director of software and product development”</p>
    <h1 class="person-name">DANA WELLS</h1>
    <p class="person-role">PRESIDENT</p>
    <address class="contact">
      418 Cedar Bend Road<br>
      Riverton, AL 36000<br>
      251.555.0148 (Dirct)<br>
      danawells@kestreltrade.com
    </address>
    <p class="brand-small">KESTREL</p>
  </section>

  <section class="card card--back" aria-label="Card back">
    <div class="accent-rule" aria-hidden="true"></div>
    <p class="brand-large">KESTREL TRADE GROUP</p>
    <p class="website">www.KestrelTrade.com</p>
  </section>
</div>
</body>
</html>
```